Our architectural studio needs a new business card

We need a business card design for our studio based in Waterloo in Belgium. We are active in architecture, design and installation.
Our works are contemporary and minimalist. our clients are refined and cultured.
Our business card must be minimalist and refined.

Project Deadline Extended
Reason: Some designers have accepted my invitation but they don't have all replied. I want to give them a chance to make one proposal. Paul

Target Market(s)

architecture

Industry/Entity Type

Business

Contact Information for Business Card

studio: paul dornevaux studio
paul dornevaux, architecte
M. +32 471 586 927
F. +322 619 4850
www.pauldornevaux-example.com
paul@pauldornevaux-example.com
14 rue des Marronniers
1420 Waterloo
Belgium

Font styles to use
Sans Serif

Requirements
Must have
• simple, minimalist, clear, elegant and chic! Black and white
Nice to have
• embossed logo, other format like a square for example
Should not have
• color, fantasy, curves, ...

```html
<!DOCTYPE html>
<html lang="en">
<head>
<meta charset="utf-8">
<title>Paul Dornevaux Studio — Business Card</title>
<link href="https://fonts.googleapis.com/css2?family=Roboto+Condensed:wght@400;700&display=swap" rel="stylesheet">
<style>
  :root {
    --page: #ffffff;
    --ink: #111111;
    --card-dark: #0a0a0a;
    --card-light: #ffffff;
    --paper-edge: #b9b9b9;
    --reverse: #ffffff;
    --muted: #555555;
  }
  html, body {
    margin: 0;
    padding: 0;
    width: 1200px;
    height: 1122px;
    overflow: hidden;
    background: var(--page);
    font-family: "Roboto Condensed", Arial, sans-serif;
  }
  .canvas {
    position: relative;
    width: 1200px;
    height: 1122px;
  }
  .card {
    position: absolute;
    top: 116px;
    height: 200px;
    box-sizing: border-box;
  }
  .card-front {
    left: 209px;
    width: 360px;
    background: var(--card-dark);
    color: var(--reverse);
  }
  .card-back {
    left: 603px;
    width: 321px;
    height: 202px;
    background: var(--card-light);
    border: 1px solid var(--paper-edge);
    color: var(--ink);
  }

  /* front */
  .front-wordmark {
    position: absolute;
    left: 0;
    right: 0;
    top: 140px;
    display: flex;
    justify-content: center;
    align-items: center;
    gap: 10px;
  }
  .front-wordmark .mark-square {
    width: 9px;
    height: 9px;
    background: var(--reverse);
  }
  .front-wordmark .studio-name {
    font-size: 10px;
    font-weight: 700;
    letter-spacing: 3.2px;
    text-transform: uppercase;
    white-space: nowrap;
  }

  /* back */
  .back-wordmark {
    position: absolute;
    left: 46px;
    top: 62px;
    width: 110px;
    display: flex;
    flex-direction: column;
    align-items: center;
    gap: 20px;
  }
  .back-wordmark .mark-square {
    width: 18px;
    height: 18px;
    background: var(--ink);
  }
  .back-wordmark .studio-name {
    font-size: 5.5px;
    font-weight: 700;
    letter-spacing: 1.6px;
    text-transform: uppercase;
    white-space: nowrap;
  }
  .contact {
    position: absolute;
    left: 162px;
    top: 56px;
  }
  .contact .person {
    margin: 0;
    font-size: 16px;
    font-weight: 700;
    line-height: 1;
    text-transform: uppercase;
    letter-spacing: 0.2px;
  }
  .contact .role {
    margin: 1px 0 0;
    font-size: 10px;
    line-height: 1;
    text-transform: uppercase;
    letter-spacing: 0.6px;
  }
  .contact-list {
    list-style: none;
    margin: 11px 0 0;
    padding: 0;
  }
  .contact-list li {
    position: relative;
    padding-left: 9px;
    margin-bottom: 6px;
    font-size: 9.5px;
    line-height: 10px;
    font-weight: 700;
  }
  .contact-list li::before {
    content: "";
    position: absolute;
    left: 0;
    top: 3px;
    width: 3px;
    height: 3px;
    border-radius: 50%;
    background: var(--ink);
  }
  .contact-list .label {
    font-size: 6px;
    font-weight: 400;
    letter-spacing: 0.4px;
    color: var(--muted);
    text-transform: uppercase;
  }
  .contact-list .indent {
    display: block;
    padding-left: 32px;
  }
</style>
</head>
<body>
<main class="canvas">
  <section class="card card-front" aria-label="Card front">
    <div class="front-wordmark">
      <span class="mark-square"></span>
      <span class="studio-name">Paul Dornevaux Studio</span>
    </div>
  </section>

  <section class="card card-back" aria-label="Card back">
    <div class="back-wordmark">
      <span class="mark-square"></span>
      <span class="studio-name">Paul Dornevaux Studio</span>
    </div>
    <div class="contact">
      <h1 class="person">Paul Dornevaux</h1>
      <p class="role">Architecte</p>
      <ul class="contact-list">
        <li>M. +32 471 586 927<br>F. +322 619 4850</li>
        <li>www.pauldornevaux-example.com<br>paul@pauldornevaux-example.com</li>
        <li><span class="label">Address</span> 14 rue des Marronniers 1420<span class="indent">Waterloo Belgium</span></li>
      </ul>
    </div>
  </section>
</main>
</body>
</html>
```